KEV.PRO- Darren Holcombe Fitness- needs a clever business card using the logo, name, info, contact

I need a business card designed for my Online Personal Training company called KEV.PRO, abbreviation for Darren Holcombe Fitness. My company focuses on coaching in personal health and personal growth to unleash your greatest potential. I would like to see designs that use my color scheme of a redish-orange (C:0,M:84,Y:100,K:0), grey, white, black, and my company font is OSWALD. The final design should communicate some aspects of design, health, motivation, growth, in some way. The logo is very important to the company and can be displayed in any of the colors previously mentioned. Must include the company name, my website: www.kev-pro.example , my email: dan@kev-pro.example

Target Market(s)

Personal health, fitness, general public, those who lack knowledge, awareness, and confidence in personal health

Industry/Entity Type

Personal Trainer

Font styles to use
Other font styles liked:
• OSWALD. (Bold, Regular, Light)

Colors
f37122
ffffff
9d9d9d
000000

Requirements
Must have
• Must include the logo, company name, my website: www.kev-pro.example , my email: dan@kev-pro.example
Nice to have
• Variations of the colors scheme of a redish-orange (C:0,M:84,Y:100,K:0), grey, white, black. Logo, card, or text can be in any of these colors.
• Possible quote like "Take control of your personal health to unleash your greatest potential" or "Unleashing your greatness first begins with fitness of the body and mind"

```html
<!DOCTYPE html>
<html lang="en">
<head>
<meta charset="utf-8">
<title>KEV.PRO Business Card</title>
<link href="https://fonts.googleapis.com/css2?family=Oswald:wght@300;400;700&family=Roboto+Condensed:ital,wght@0,400;1,400&display=swap" rel="stylesheet">
<style>
  :root {
    --orange: #f37122;
    --white: #ffffff;
    --paper: #f6f6f6;
    --grey: #9d9d9d;
    --ink: #2a2a2a;
    --card-dark: #231f20;
    --stage: #3a3a3a;
  }
  * { margin: 0; padding: 0; box-sizing: border-box; }
  html, body { width: 1200px; height: 911px; overflow: hidden; }
  body { background: var(--stage); position: relative; font-family: "Oswald", sans-serif; }

  .card {
    position: absolute;
    width: 560px;
    height: 320px;
    box-shadow: 0 10px 30px rgba(0,0,0,.35);
  }
  .card--front { left: 90px; top: 110px; background: var(--paper); }
  .card--back { left: 550px; top: 480px; background: var(--card-dark); }

  /* brand lockup */
  .brand { position: absolute; display: flex; align-items: center; gap: 14px; }
  .brand__dot { width: 46px; height: 46px; border-radius: 50%; }
  .brand__name { font-weight: 700; font-size: 44px; line-height: 1; letter-spacing: .5px; }
  .brand__sub { font-weight: 300; font-size: 10px; letter-spacing: 1.2px; text-transform: uppercase; margin-top: 4px; }

  .card--front .brand { left: 40px; bottom: 44px; }
  .card--front .brand__dot { background: var(--orange); }
  .card--front .brand__name { color: var(--ink); }
  .card--front .brand__sub { color: var(--grey); }

  .card--back .brand { left: 50%; top: 74px; transform: translateX(-50%); }
  .card--back .brand__dot { background: var(--white); }
  .card--back .brand__name { color: var(--white); }
  .card--back .brand__sub { color: var(--grey); }

  /* contact block */
  .contact { position: absolute; right: 40px; top: 40px; width: 200px; }
  .contact__name { color: var(--orange); font-weight: 400; font-size: 22px; line-height: 1.1; text-transform: uppercase; }
  .contact__role { color: var(--ink); font-weight: 400; font-size: 17px; text-transform: uppercase; margin-top: 2px; }
  .contact__rule { height: 2px; background: var(--orange); margin: 10px 0 12px; }
  .contact__list { list-style: none; }
  .contact__item { display: flex; align-items: center; gap: 8px; color: #555; font-family: "Roboto Condensed", sans-serif; font-size: 14px; line-height: 22px; }
  .contact__icon { width: 12px; height: 12px; flex: none; }

  /* tagline */
  .tagline {
    position: absolute; left: 36px; right: 36px; bottom: 40px;
    color: var(--white); font-family: "Roboto Condensed", sans-serif; font-style: italic;
    font-size: 15px; line-height: 1.45;
  }
</style>
</head>
<body>

<section class="card card--front" aria-label="Business card front">
  <div class="brand">
    <span class="brand__dot"></span>
    <div>
      <div class="brand__name">KEV.PRO</div>
      <div class="brand__sub">Darren Holcombe Fitness</div>
    </div>
  </div>

  <div class="contact">
    <div class="contact__name">Alex Rivera</div>
    <div class="contact__role">CEO/Founder</div>
    <div class="contact__rule"></div>
    <ul class="contact__list">
      <li class="contact__item">
        <svg class="contact__icon" viewBox="0 0 12 12" aria-hidden="true"><path d="M2.5 1 L4.5 1 L5 3.5 L3.8 4.5 C4.5 6 6 7.5 7.5 8.2 L8.5 7 L11 7.5 L11 9.5 C11 10.5 10 11 9 11 C4.5 10.5 1.5 7.5 1 3 C1 2 1.5 1 2.5 1 Z" fill="#f37122"/></svg>
        555 014 2290
      </li>
      <li class="contact__item">
        <svg class="contact__icon" viewBox="0 0 12 12" aria-hidden="true"><rect x="1" y="2.5" width="10" height="7" fill="#f37122"/><path d="M1 2.5 L6 6.5 L11 2.5" stroke="#f6f6f6" stroke-width="1" fill="none"/></svg>
        dan@kev-pro.example
      </li>
      <li class="contact__item">
        <svg class="contact__icon" viewBox="0 0 12 12" aria-hidden="true"><circle cx="6" cy="6" r="5.5" fill="#f37122"/><path d="M0.5 6 H11.5 M6 0.5 C3.5 3 3.5 9 6 11.5 M6 0.5 C8.5 3 8.5 9 6 11.5" stroke="#f6f6f6" stroke-width=".8" fill="none"/></svg>
        www.kev-pro.example
      </li>
    </ul>
  </div>
</section>

<section class="card card--back" aria-label="Business card back">
  <div class="brand">
    <span class="brand__dot"></span>
    <div>
      <div class="brand__name">KEV.PRO</div>
      <div class="brand__sub">Darren Holcombe Fitness</div>
    </div>
  </div>
  <p class="tagline">Take control of your personal health to unleash your greatest potential<br>Unleashing your greatness first begins with fitness of the body and mind</p>
</section>

</body>
</html>
```